Business Card Design Project

We require business cards for "Venmoor". We are composed of elite prior military personnel. Our goal is to provide site security for premium businesses who want on the most professional of agents on their premises. Additionally, we will provide executive protection for individuals who require professionalism, flexibility, and dedication

We want this business card to communicate professionalism, dependability, strength. However, we are not an overtly tactical agency and do not want to intimidate our clients personnel or their client. We want to give them a sense of security.
Updates

At the request of one of the designers I've listed the appropriate text that should appear on the card. Please feel free to arrange it in a creative and professional manor.

I've also uploaded a .png file of the triangle logo with no text. Please feel free to incorporate this into your designs.

ThanksĀ 

Target Market(s)

Premium businesses, executives, celebrities, and governments.

Industry/Entity Type

Security

Requirements
Must have
• Text Info that will go on the card. It does not have to be in this order:
Name
Title
Office Phone Number
Cell Phone Number
Email
Website
Mailing Address
Nice to have
• On the back I'd like to see the triangle portion of the logo displayed in a creative way that leaves enough room to write down information if needed.
Should not have
• - Weapons, Globes, or Shields. Every rent-a-cop company has that, and that's not what we are.

```html
<!DOCTYPE html>
<html lang="en">
<head>
<meta charset="utf-8">
<title>Venmoor Business Card</title>
<link href="https://fonts.googleapis.com/css2?family=Open+Sans:wght@400;700;800&display=swap" rel="stylesheet">
<style>
  :root {
    --stage: #262626;
    --paper: #ffffff;
    --paper-shade: #eef1f3;
    --brand-blue: #1f86c6;
    --brand-blue-deep: #1467a3;
    --ink: #4a4a4a;
    --ink-soft: #6d6d6d;
    --back-card: #2e2e2e;
    --back-text: #e9e9e9;
    --back-muted: #9a9a9a;
  }
  * { margin: 0; padding: 0; box-sizing: border-box; }
  html, body {
    width: 1200px; height: 900px; overflow: hidden;
    background: var(--stage);
    font-family: "Open Sans", Arial, sans-serif;
  }
  .canvas {
    width: 1200px; height: 900px;
    display: flex; flex-direction: column;
    align-items: center; justify-content: center; gap: 36px;
  }
  .card {
    position: relative; width: 700px; height: 400px; overflow: hidden;
    box-shadow: 0 14px 34px rgba(0,0,0,.55);
  }
  /* Front */
  .card-front { background: linear-gradient(180deg, var(--paper), var(--paper-shade)); }
  .card-front .band { position: absolute; inset: 0; }
  .front-brand {
    position: absolute; left: 70px; top: 118px;
    display: flex; align-items: center; gap: 12px;
  }
  .brand-dot { width: 22px; height: 22px; background: var(--brand-blue); }
  .brand-name {
    font-weight: 800; font-size: 30px; letter-spacing: 1px;
    color: var(--ink); text-transform: uppercase;
  }
  .holder { position: absolute; left: 104px; top: 178px; }
  .holder-name { font-size: 22px; color: var(--ink); line-height: 1.1; }
  .holder-title { font-size: 16px; color: var(--brand-blue); }
  .side-tab {
    position: absolute; left: 0; top: 212px; width: 16px; height: 26px;
    background: var(--brand-blue); border-radius: 0 6px 6px 0;
  }
  .address {
    position: absolute; left: 70px; bottom: 34px;
    font-size: 17px; line-height: 1.2; color: var(--brand-blue-deep);
  }
  .contacts {
    position: absolute; right: 22px; top: 98px;
    list-style: none; font-size: 12px; line-height: 19px;
    color: var(--paper); text-align: right;
  }
  .contacts li { display: flex; justify-content: flex-end; align-items: center; gap: 8px; }
  .contacts svg { width: 12px; height: 12px; fill: var(--paper); }
  /* Back */
  .card-back { background: var(--back-card); }
  .back-brand {
    position: absolute; left: 50%; top: 150px; transform: translateX(-50%);
    display: flex; align-items: center; gap: 20px;
  }
  .back-brand .brand-dot { width: 44px; height: 44px; }
  .back-brand .brand-name { font-size: 62px; color: var(--back-text); letter-spacing: 2px; }
  .back-web {
    position: absolute; left: 0; right: 0; bottom: 40px;
    text-align: center; font-size: 17px; color: var(--back-muted);
  }
</style>
</head>
<body>
<main class="canvas">
  <section class="card card-front">
    <svg class="band" viewBox="0 0 700 400" preserveAspectRatio="none" aria-hidden="true">
      <path d="M0,285 C240,250 500,200 590,80 Q625,30 700,22 L700,350 C470,362 230,380 0,400 Z" fill="var(--brand-blue)"/>
    </svg>
    <div class="front-brand">
      <span class="brand-dot"></span>
      <span class="brand-name">Venmoor</span>
    </div>
    <div class="holder">
      <p class="holder-name">Your Name</p>
      <p class="holder-title">manager</p>
    </div>
    <span class="side-tab"></span>
    <p class="address">Street, City<br>Country</p>
    <ul class="contacts">
      <li>012 345 6789 <svg viewBox="0 0 12 12"><path d="M2 1h3l1 3-2 1a7 7 0 0 0 3 3l1-2 3 1v3c0 1-1 1-2 1A10 10 0 0 1 1 3c0-1 0-2 1-2z"/></svg></li>
      <li>012 345 6789 <svg viewBox="0 0 12 12"><rect x="3" y="0" width="6" height="12" rx="1"/></svg></li>
      <li>info@venmoor.com <svg viewBox="0 0 12 12"><rect x="0" y="2" width="12" height="8"/></svg></li>
      <li>/venmoor <svg viewBox="0 0 12 12"><circle cx="6" cy="6" r="5"/></svg></li>
      <li>www.venmoor.com <svg viewBox="0 0 12 12"><circle cx="6" cy="6" r="5"/></svg></li>
    </ul>
  </section>

  <section class="card card-back">
    <div class="back-brand">
      <span class="brand-dot"></span>
      <span class="brand-name">Venmoor</span>
    </div>
    <p class="back-web">www.venmoor.com</p>
  </section>
</main>
</body>
</html>
```